Wheels 4 Hire Car Co-Hosting program

I want to create an ad on Pictora, graphic design with my company name is Wheels 4 Hire . I am a host on the Vexa platform and I rent my cars out.
I have 90+ cars..
I’m trying to reach people that Have an extra car laying around or just tired of their car but are stuck with the payments.
And tell them Unlock earning potential with your car!
List it on our fleet for hassle-free renting on Vexa.
We manage A-Z and you profit.
Start now!
Dm us year, make, model and current mileage on odometer to find out if you qualify!
Vehicle must have a clean title and must be registered to you!

Target Market(s)

People that have an extra car laying around or are tired of their car and warm to get into a new car but they are stuck with the payments of their original car. We can take their car and rent it out for them.

Industry/Entity Type

Car rental fleet management

Requirements
Must have
• Car rental, money, profit, etc

```html
<!DOCTYPE html>
<html lang="en">
<head>
<meta charset="utf-8">
<title>Wheels 4 Hire – Co-Hosting Program</title>
<link rel="stylesheet" href="https://fonts.googleapis.com/css2?family=Poppins:ital,wght@0,600;0,700;1,300;1,400;1,500&display=swap">
<style>
  :root {
    --charcoal: #1c1b1f;
    --charcoal-soft: #2c2b30;
    --red-deep: #8c1a1d;
    --red-mid: #b3262a;
    --red-bright: #e2363b;
    --paper: #f6f6f6;
    --ink: #111111;
    --ink-soft: #444444;
    --white: #ffffff;
    --car-blue: #2e86cf;
    --car-black: #1a1b1f;
    --car-silver: #b9bcc0;
  }
  * { margin: 0; padding: 0; box-sizing: border-box; }
  html, body { width: 1200px; height: 1200px; overflow: hidden; background: var(--paper); }
  .ad {
    position: relative;
    width: 1200px;
    height: 1200px;
    overflow: hidden;
    background: var(--paper);
    font-family: "Poppins", "Century Gothic", sans-serif;
    color: var(--white);
  }
  .ad__backdrop {
    position: absolute;
    left: 0; top: 0;
    width: 1200px; height: 690px;
    background:
      radial-gradient(ellipse 360px 420px at 760px 300px, rgba(140,26,29,0.8), rgba(90,20,24,0.3) 60%, transparent 82%),
      linear-gradient(180deg, var(--charcoal-soft) 0%, var(--charcoal) 82%, rgba(28,27,31,0) 100%);
  }
  .ad__headline {
    position: absolute;
    left: 80px; top: 112px;
    font-style: italic;
    font-weight: 500;
    font-size: 57px;
    line-height: 58px;
    letter-spacing: -0.5px;
  }
  .ad__subline {
    position: absolute;
    left: 84px; top: 262px;
    font-style: italic;
    font-weight: 300;
    font-size: 44px;
    line-height: 46px;
  }
  .ad__brand {
    position: absolute;
    left: 890px; top: 76px;
    width: 240px;
    text-align: center;
    font-weight: 700;
    font-size: 44px;
    line-height: 46px;
    letter-spacing: 0.5px;
    color: var(--white);
  }
  .ad__fleet {
    position: absolute;
    left: 110px; top: 510px;
    width: 1090px; height: 390px;
    border-radius: 90px 0 0 30px;
    background:
      linear-gradient(90deg,
        var(--car-blue) 0%, #1f6fb8 24%,
        var(--car-black) 30%, #2a2b30 62%,
        var(--car-silver) 68%, #cfd1d4 100%);
  }
  .ad__badge {
    position: absolute;
    left: 857px; top: 262px;
    width: 323px; height: 322px;
    border-radius: 50% 0 50% 50%;
    background: linear-gradient(165deg, var(--red-deep) 0%, var(--red-mid) 55%, var(--red-bright) 100%);
    text-align: center;
    font-style: italic;
    font-weight: 500;
  }
  .ad__badge-small { position: absolute; left: 0; right: 0; top: 86px; font-size: 30px; letter-spacing: -0.5px; }
  .ad__badge-large { position: absolute; left: 0; right: 0; top: 126px; font-size: 50px; line-height: 52px; }
  .ad__cta {
    position: absolute;
    left: 382px; top: 914px;
    width: 435px; height: 104px;
    border-radius: 52px 52px 52px 0;
    background: linear-gradient(180deg, var(--red-bright) 0%, var(--red-deep) 100%);
    color: var(--white);
    font-style: italic;
    font-weight: 400;
    font-size: 54px;
    line-height: 104px;
    text-align: center;
    letter-spacing: -1px;
  }
  .ad__note {
    position: absolute;
    left: 0; right: 0; top: 1046px;
    text-align: center;
    color: var(--ink);
    font-style: italic;
    font-weight: 400;
    font-size: 41px;
    line-height: 44px;
  }
  .ad__terms {
    position: absolute;
    left: 0; right: 0; top: 1150px;
    text-align: center;
    color: var(--ink-soft);
    font-style: italic;
    font-weight: 300;
    font-size: 21px;
    line-height: 26px;
  }
</style>
</head>
<body>
  <main class="ad">
    <div class="ad__backdrop" role="img" aria-label="Dark studio photo of a red car's headlight close up"></div>

    <h1 class="ad__headline">Unlock Earning<br>Potential With Your Car!</h1>
    <p class="ad__subline">List it on our fleet for<br>hassle-free renting<br>on Vexa.</p>

    <div class="ad__brand">WHEELS<br>4 HIRE</div>

    <div class="ad__fleet" role="img" aria-label="Photo of three rental cars side by side: a blue hatchback, a black sedan and a silver sedan"></div>

    <div class="ad__badge">
      <span class="ad__badge-small">WE MANAGE A-Z</span>
      <span class="ad__badge-large">AND YOU<br>PROFIT!</span>
    </div>

    <div class="ad__cta">START NOW!</div>

    <p class="ad__note">Dm us year, make, model and current mileage<br>on odometer to find out if you qualify!</p>
    <p class="ad__terms">Vehicle must have a clean title and must be registered to you!</p>
  </main>
</body>
</html>
```